Professional violinist needs business cards

I am trying to attract the following jobs:
-private violin lessons (primarily classical)
-performance gigs (weddings, birthday parties, funerals, etc.)
-collaborations with other artists (studio recordings, performances)

I want to communicate that I have a very high standard of excellence for my work, but I also love people and celebrations.
Values/style words I like are:
love, joy, peace, fun, beauty, authenticity, excellence, warmth, refined/sleek, free spirited. If that's too confusing, just ignore :)

I will attach my favorite business card template that I could find on Canva. The lines are supposed to be like a music staff, which I think is really cool, but I also don't want it to look too busy. I like the simple black and white--I think it looks sharp--but I also am open to other ideas. I also have seen business cards with pictures included that looked great, so I attached an image that could be used as well.

I am also attaching a file that I made of my initials that could be used as a logo, but I'm not sure if it should be included.

Information on the card:
-My name (18 letters total)
-"violinist"
-phone number, email, website

Thank you!

```html
<!DOCTYPE html>
<html lang="en">
<head>
<meta charset="utf-8">
<title>Marianne Ellsworth – Violinist business cards</title>
<link rel="stylesheet" href="https://fonts.googleapis.com/css2?family=Dancing+Script:wght@500&family=Lora:wght@400&family=Cinzel:wght@400&display=swap">
<style>
  :root{
    --stage:#2b2b2c;
    --card:#22262a;
    --card-deep:#1b1e21;
    --cream:#d8ccb0;
    --ivory:#eeeae2;
    --photo-warm:#6b5a45;
    --photo-dark:#2a2620;
  }
  *{margin:0;padding:0;box-sizing:border-box}
  html,body{width:1200px;height:1138px;overflow:hidden}
  body{background:var(--stage);position:relative;font-family:"Lora",serif}
  .card{position:absolute;width:620px;height:374px;border-radius:14px;overflow:hidden;background:var(--card);box-shadow:0 6px 14px rgba(0,0,0,.45)}
  .card--front{left:274px;top:186px}
  .card--back{left:276px;top:608px}

  .front-photo{position:absolute;left:0;top:0;width:240px;height:100%;
    background:linear-gradient(90deg,var(--photo-warm) 0%,#4f4334 55%,var(--card) 100%)}
  .front-photo::after{content:"";position:absolute;inset:0;
    background:radial-gradient(ellipse 40% 60% at 45% 55%,rgba(20,18,16,.75),transparent 70%)}

  .monogram{font-family:"Lora",serif;color:var(--cream);font-size:40px;letter-spacing:2px;line-height:1;white-space:nowrap}
  .name{font-family:"Dancing Script",cursive;font-weight:500;color:var(--ivory);font-size:40px;white-space:nowrap;line-height:1}
  .title-row{display:flex;align-items:center;gap:14px;margin-top:8px}
  .title-row .rule{height:1px;background:var(--cream);opacity:.8;flex:0 0 70px}
  .role{font-family:"Cinzel",serif;color:var(--ivory);font-size:16.5px;letter-spacing:3px;white-space:nowrap}

  .front-identity{position:absolute;left:274px;top:120px;width:320px;display:flex;flex-direction:column;align-items:center}
  .front-identity .monogram{margin-bottom:28px}

  .back-photo{position:absolute;inset:0;
    background:radial-gradient(ellipse 22% 80% at 52% 55%,#15171a 0%,transparent 80%),
               linear-gradient(180deg,#2e2e2b 0%,#26282a 50%,#1f2225 100%)}
  .staff{position:absolute;left:0;right:0;height:7px;border-top:2px solid var(--cream);border-bottom:2px solid var(--cream);opacity:.9}
  .staff--top{top:20px}
  .staff--bottom{top:344px}

  .back-identity{position:absolute;left:102px;top:92px;display:flex;align-items:center;gap:28px}
  .back-identity .monogram{font-size:50px}
  .back-identity .stack{display:flex;flex-direction:column;align-items:center}

  .contact{position:absolute;left:109px;width:400px;top:194px;text-align:center;color:var(--ivory);font-size:15.5px;line-height:23px}
  .contact .accent{color:var(--cream)}
</style>
</head>
<body>
  <section class="card card--front">
    <div class="front-photo" role="img" aria-label="Portrait of the violinist in a black dress holding a violin and bow beside a stone wall and stair rail"></div>
    <div class="front-identity">
      <div class="monogram">ME</div>
      <div class="name">Marianne Ellsworth</div>
      <div class="title-row"><span class="rule"></span><span class="role">VIOLINIST</span><span class="rule"></span></div>
    </div>
  </section>

  <section class="card card--back">
    <div class="back-photo" role="img" aria-label="Darkened close view of the violinist holding a violin by a stone wall"></div>
    <div class="staff staff--top"></div>
    <div class="staff staff--bottom"></div>
    <div class="back-identity">
      <div class="monogram">ME</div>
      <div class="stack">
        <div class="name">Marianne Ellsworth</div>
        <div class="title-row"><span class="rule"></span><span class="role">VIOLINIST</span><span class="rule"></span></div>
      </div>
    </div>
    <div class="contact">
      <p>+1 (555) 014-2876</p>
      <p>Marianne@MarianneEllsworth.com</p>
      <p>www.<span class="accent">MarianneEllsworth</span>.com</p>
      <p>Larkfield, VA</p>
    </div>
  </section>
</body>
</html>
```